Velloria Flowers Florist Flyer

We are requiring a flyer that advertises and promotes our new business. We specialise in weddings and events but would also like to branch out to corporates and an online subscription. Our brand is feminine/romantic with a touch of elegance and luxury. Our main colour schemes are white, black, gold and pale pink. Instagram: Velloria_flowers and website www.velloriaflowers.com.au
Target Market(s)
brides to be, females
Industry/Entity Type
Florist
Font styles to use
Sans Serif
Script
Other font styles liked:
- The Carpenter
Colors
ffffff
000000
333333
Requirements
Must have
- Feminine/romantic feel, through use of theme colours and elegant font
- our contact details Ph: 0429518064
- email address: contactus@velloriaflowers.com.au
Nice to have
- a description of us willing to work with clients to create their dream wedding flowers. That we offer consultations and no obligation quotes.

```html
<!DOCTYPE html>
<html lang="en">
<head>
<meta charset="utf-8">
<title>Velloria Flowers Flyer</title>
<link rel="stylesheet" href="https://fonts.googleapis.com/css2?family=Lato:wght@400;700&family=Cardo:wght@400;700&family=Dancing+Script:wght@500&family=Jost:ital,wght@1,400&display=swap">
<style>
  :root {
    --pink: #e783b6;
    --pink-light: #eea9cb;
    --pink-text: #ef9cc7;
    --black: #000000;
    --ink: #222222;
    --white: #ffffff;
    --panel: #f5f5f5;
    --stage: #8d8d8d;
  }
  * { margin: 0; padding: 0; box-sizing: border-box; }
  html, body { width: 1200px; height: 1200px; overflow: hidden; background: var(--stage); }
  .flyer {
    position: absolute; left: 187px; top: 20px;
    width: 885px; height: 1243px;
    transform: scale(0.9332); transform-origin: top left;
    background: var(--white); overflow: hidden;
    font-family: "Lato", sans-serif; color: var(--ink);
  }
  .backdrop { position: absolute; inset: 0; }
  .about-panel { position: absolute; left: 0; top: 640px; width: 445px; height: 490px; background: var(--panel); }

  .logo { position: absolute; left: 48px; top: 60px; font-family: "Lato", sans-serif; font-weight: 400; color: var(--black); }
  .logo__name { font-size: 64px; line-height: 1; }
  .logo__sub { font-size: 22px; letter-spacing: 19px; margin-top: 26px; }

  .hero-title { position: absolute; right: 42px; top: 282px; text-align: right; font-family: "Cardo", serif; font-weight: 700; color: var(--black); }
  .hero-title__name { font-size: 58px; line-height: 1.1; }
  .hero-title__sub { font-size: 46px; line-height: 1.1; }
  .tagline { position: absolute; right: 42px; top: 424px; text-align: right; font-family: "Cardo", serif; color: var(--white); font-size: 27px; line-height: 35px; }

  .photo-ring { position: absolute; border-radius: 50%; background: var(--white); box-shadow: 0 4px 10px rgba(0,0,0,.35); }
  .photo-ring .photo { position: absolute; inset: 8px; border-radius: 50%; }
  .ring-large { left: 308px; top: 340px; width: 256px; height: 256px; }
  .ring-large .photo { background: radial-gradient(circle at 45% 50%, #c8283a 0 12%, #f0efe0 22%, #3d5a2c 48%, #b46a3c 70%, #9aa0a0 100%); }
  .ring-small { left: 553px; top: 513px; width: 192px; height: 192px; }
  .ring-small .photo { background: radial-gradient(circle at 50% 45%, #f3a5b5 0 25%, #e97b95 40%, #4a6a3c 65%, #8b9095 100%); }

  .tab { position: absolute; top: 728px; height: 38px; padding-left: 40px; border-radius: 0 20px 20px 0;
    background: linear-gradient(90deg, var(--pink), var(--pink-light)); color: var(--white);
    font-size: 26px; font-weight: 400; line-height: 38px; box-shadow: 2px 2px 3px rgba(0,0,0,.15); }
  .tab-about { left: 0; width: 196px; }
  .tab-services { left: 445px; width: 190px; padding-left: 15px; }

  .quote { position: absolute; left: 38px; top: 768px; width: 390px; font-family: "Dancing Script", cursive; font-size: 25px; line-height: 26px; color: var(--black); }
  .quote-author { position: absolute; left: 40px; top: 870px; font-size: 17px; color: var(--black); }
  .about-copy { position: absolute; left: 40px; top: 897px; width: 380px; font-size: 15.2px; line-height: 19.2px; text-align: justify; color: var(--ink); }
  .about-copy p + p { margin-top: 10px; }

  .service { position: absolute; display: flex; align-items: center; gap: 16px; font-size: 21px; color: var(--black); }
  .service svg { width: 50px; height: 50px; }
  .svc-weddings { left: 459px; top: 775px; }
  .svc-events { left: 659px; top: 775px; }
  .svc-business { left: 459px; top: 839px; gap: 12px; }
  .svc-home { left: 659px; top: 839px; }

  .cta-heading { position: absolute; left: 461px; top: 935px; width: 400px; font-family: "Jost", sans-serif; font-style: italic; font-size: 25px; line-height: 31px; color: var(--pink-text); }
  .cta-copy { position: absolute; left: 461px; top: 1008px; width: 380px; font-size: 15.2px; line-height: 19.2px; color: var(--black); }

  .footer { position: absolute; left: 0; top: 1125px; width: 885px; height: 118px; background: linear-gradient(90deg, var(--pink), var(--pink-light)); }
  .call-box { position: absolute; left: 270px; top: 1110px; width: 327px; height: 69px; background: var(--black); color: var(--white); font-size: 28px; line-height: 69px; text-align: center; }
  .contact { position: absolute; top: 1189px; display: flex; align-items: center; gap: 9px; color: var(--white); font-size: 16.5px; }
  .contact svg { width: 20px; height: 16px; }
  .contact-email { left: 42px; }
  .contact-web { left: 578px; }
</style>
</head>
<body>
<div class="flyer">
  <div class="about-panel"></div>

  <svg class="backdrop" width="885" height="1243" viewBox="0 0 885 1243">
    <defs>
      <linearGradient id="band" x1="0" x2="1" y1="0" y2="0">
        <stop offset="0" stop-color="#e67fb3"/>
        <stop offset="1" stop-color="#eeacca"/>
      </linearGradient>
      <linearGradient id="venue" x1="0" x2="1" y1="0" y2="1">
        <stop offset="0" stop-color="#2f3a2a"/>
        <stop offset=".5" stop-color="#e9d7c4"/>
        <stop offset="1" stop-color="#4b4f48"/>
      </linearGradient>
      <radialGradient id="bouquet" cx=".55" cy=".5" r=".6">
        <stop offset="0" stop-color="#f4dccd"/>
        <stop offset=".55" stop-color="#ecdcd0"/>
        <stop offset="1" stop-color="#a9a9a9"/>
      </radialGradient>
    </defs>
    <path class="band" fill="url(#band)" d="M0,335 C80,250 190,215 290,222 C380,228 430,262 455,278 L885,120 L885,620 C780,595 650,550 530,515 L0,520 Z"/>
    <path role="img" aria-label="Photo of a large rose and lily arrangement in a reception venue" fill="url(#venue)" d="M560,0 L885,0 L885,120 C790,190 640,262 455,278 C470,170 510,70 560,0 Z"/>
    <ellipse role="img" aria-label="Photo of a cream and blush rose bridal bouquet" cx="175" cy="510" rx="265" ry="178" fill="url(#bouquet)" stroke="#3a3a3a" stroke-width="10"/>
  </svg>

  <div class="logo">
    <div class="logo__name">Velloria</div>
    <div class="logo__sub">FLOWERS</div>
  </div>

  <div class="hero-title">
    <div class="hero-title__name">Velloria</div>
    <div class="hero-title__sub">FLOWERS</div>
  </div>
  <div class="tagline">Creating stunning<br>Flowers for Weddings<br>and Events</div>

  <div class="photo-ring ring-large"><div class="photo" role="img" aria-label="Photo of a red rose, anthurium and magnolia leaf arrangement"></div></div>
  <div class="photo-ring ring-small"><div class="photo" role="img" aria-label="Photo of a pink rose cascading bouquet"></div></div>

  <div class="tab tab-about">ABOUT US</div>
  <p class="quote">Design is not making beauty, beauty emerges from selection, affinities, integration, love.</p>
  <p class="quote-author">___LAURENT KEANE</p>
  <div class="about-copy">
    <p>For generations we've been creating flowers for family and friends. Over the years this has been our test bed for creating our design pieces for weddings and events. Now we want to make our beautiful creations available to everyone.</p>
    <p>Our designers have had extensive backgrounds, from owning a florist, to chocolate bouquet design and creations. Our friends and family loved working with our designers to create their perfect flower design, no matter what the event was.</p>
  </div>

  <div class="tab tab-services">SERVICES</div>
  <div class="service svc-weddings">
    <svg viewBox="0 0 50 50" fill="none" stroke="#e783b6" stroke-width="2"><circle cx="25" cy="25" r="23"/><path d="M25 36 C14 28 11 23 13 18 C15 13 22 13 25 19 C28 13 35 13 37 18 C39 23 36 28 25 36 Z"/></svg>
    <span>Weddings</span>
  </div>
  <div class="service svc-events">
    <svg viewBox="0 0 50 50" fill="none" stroke="#e783b6" stroke-width="2"><circle cx="25" cy="25" r="23"/><rect x="14" y="16" width="22" height="19" rx="1"/><line x1="14" y1="21" x2="36" y2="21"/><line x1="19" y1="13" x2="19" y2="18"/><line x1="31" y1="13" x2="31" y2="18"/><path d="M25 24 l1.4 3 3 .3 -2.3 2 .7 3 -2.8-1.6 -2.8 1.6 .7-3 -2.3-2 3-.3 Z" stroke-width="1.2"/></svg>
    <span>Events</span>
  </div>
  <div class="service svc-business">
    <svg viewBox="0 0 50 50" fill="none" stroke="#e783b6" stroke-width="2"><circle cx="25" cy="25" r="23"/><rect x="13" y="18" width="24" height="16" rx="2" fill="#e783b6"/><path d="M21 18 v-3 h8 v3"/><line x1="13" y1="25" x2="37" y2="25" stroke="#fff"/></svg>
    <span>Businesses</span>
  </div>
  <div class="service svc-home">
    <svg viewBox="0 0 50 50" fill="none" stroke="#e783b6" stroke-width="2"><circle cx="25" cy="25" r="23"/><path d="M11 26 L25 13 L39 26" stroke-width="3"/><path d="M16 24 V36 H34 V24 L25 16 Z" fill="#e783b6"/><rect x="22" y="28" width="6" height="8" fill="#fff" stroke="none"/></svg>
    <span>Home</span>
  </div>

  <h2 class="cta-heading">LOOKING FOR FLOWERS FOR A WEDDING OR EVENT?</h2>
  <p class="cta-copy">We specialise in flowers for weddings and events. No matter how big or small we're here to create the best looking flowers just for you.</p>

  <div class="footer"></div>
  <div class="call-box">Call now: 0429518064</div>
  <div class="contact contact-email">
    <svg viewBox="0 0 20 16"><rect x="1" y="2" width="18" height="12" fill="#fff"/><path d="M1 2 L10 9 L19 2" fill="none" stroke="#e99cc2" stroke-width="1.5"/></svg>
    <span>contactus@velloriaflowers.com.au</span>
  </div>
  <div class="contact contact-web">
    <svg viewBox="0 0 16 16" fill="none" stroke="#fff" stroke-width="1.3"><circle cx="8" cy="8" r="6.5"/><ellipse cx="8" cy="8" rx="3" ry="6.5"/><line x1="1.5" y1="8" x2="14.5" y2="8"/></svg>
    <span>www.velloriaflowers.com.au</span>
  </div>
</div>
</body>
</html>
```